Business Card Design

I'm a commercial general contractor remodel offices, hotels, health clubs and stores mostly San Francisco and the peninsula
the file I down loaded is kind of what I want I like the I beam with my company name in it, that would be fine with me but if you have better Idea will look at it you never know, I'm decided to give in and change my company name to how every one knows me, I have been in business since 1991, I like the I beam logo I included one of my old card from my old company for reference for you.

Industry/Entity Type

Business

Contact Information for Business Card

BRAXO CONSTRUCTION (is my company name)
Wendell Trusk contractor, LIc 314827
4158 Garnet Row, Cedar Hollow, California 94000
mobile, (415) 555-0147
phone (650) 555-0182
Fax, (650) 555-0183
email, braxo@braxoconstruction.example

```html
<!DOCTYPE html>
<html lang="en">
<head>
<meta charset="utf-8">
<title>Braxo Construction – Business Card</title>
<link rel="stylesheet" href="https://fonts.googleapis.com/css2?family=Source+Sans+3:wght@400;600&display=swap">
<style>
  :root {
    --page-bg: #e9e9ea;
    --card-top-light: #f4f4f5;
    --card-top-dark: #c9cacc;
    --skyline: #d3d4d6;
    --band: #262627;
    --panel: #6b6c6f;
    --accent: #1a9be0;
    --text-dark: #222325;
    --text-panel: #2e2f31;
    --text-muted: #8a8b8e;
    --text-light: #d8d9db;
  }
  * { margin: 0; padding: 0; box-sizing: border-box; }
  html, body { width: 1200px; height: 800px; overflow: hidden; }
  body {
    background: var(--page-bg);
    font-family: "Source Sans 3", "Source Sans Pro", Arial, sans-serif;
    display: flex; align-items: center; justify-content: center;
  }
  .card {
    position: relative;
    width: 1050px; height: 600px;
    background: radial-gradient(ellipse at 55% 25%, var(--card-top-light) 0%, #e2e3e4 55%, var(--card-top-dark) 100%);
    box-shadow: 0 10px 30px rgba(0,0,0,.18);
    overflow: hidden;
  }
  .skyline {
    position: absolute; left: 0; right: 0; top: 170px; height: 130px;
    background: linear-gradient(to bottom, rgba(211,212,214,0) 0%, var(--skyline) 100%);
  }
  .brand {
    position: absolute; left: 290px; top: 120px;
    display: flex; align-items: center; gap: 16px;
  }
  .brand-mark { width: 26px; height: 26px; background: var(--accent); }
  .brand-name {
    font-size: 40px; font-weight: 600; letter-spacing: 4px;
    color: var(--text-dark); white-space: nowrap;
  }
  .license {
    position: absolute; right: 40px; top: 205px;
    font-size: 24px; letter-spacing: 1px; color: var(--text-muted);
    white-space: nowrap;
  }
  .name-band {
    position: absolute; left: 0; right: 0; top: 300px; height: 66px;
    background: var(--band);
    display: flex; align-items: center;
  }
  .holder-name {
    position: absolute; left: 60px;
    font-size: 34px; color: var(--accent); letter-spacing: .5px;
    white-space: nowrap;
  }
  .holder-title {
    position: absolute; left: 560px;
    font-size: 34px; color: var(--text-light); letter-spacing: .5px;
  }
  .contact-panel {
    position: absolute; left: 0; right: 0; top: 366px; bottom: 0;
    background: var(--panel);
  }
  .contact-list {
    position: absolute; list-style: none;
    display: flex; flex-direction: column; gap: 14px;
  }
  .contact-list.phones { left: 60px; top: 36px; }
  .contact-list.details { left: 520px; top: 36px; }
  .contact-list li {
    display: flex; align-items: flex-start; gap: 18px;
    font-size: 25px; line-height: 30px; color: var(--text-panel);
    white-space: nowrap;
  }
  .contact-list svg { width: 24px; height: 24px; flex: none; margin-top: 3px; }
  .icon { fill: none; stroke: var(--accent); stroke-width: 2; }
  .icon-fill { fill: var(--accent); }
</style>
</head>
<body>
  <div class="card">
    <div class="skyline" role="img" aria-label="Faint city skyline silhouette with a suspension bridge"></div>

    <div class="brand">
      <span class="brand-mark"></span>
      <span class="brand-name">BRAXO CONSTRUCTION</span>
    </div>
    <div class="license">LIC 314827</div>

    <div class="name-band">
      <span class="holder-name">WENDELL "BRAXO" TRUSK</span>
      <span class="holder-title">CONTRACTOR</span>
    </div>

    <div class="contact-panel">
      <ul class="contact-list phones">
        <li>
          <svg viewBox="0 0 24 24" aria-hidden="true"><rect class="icon" x="6" y="2" width="12" height="20" rx="2"/><circle class="icon-fill" cx="12" cy="18.5" r="1.2"/></svg>
          (415) 555-0147
        </li>
        <li>
          <svg viewBox="0 0 24 24" aria-hidden="true"><circle class="icon" cx="12" cy="12" r="10"/><path class="icon-fill" d="M9 6.5l2 2.5-1.3 1.3a7 7 0 0 0 4 4L15 13l2.5 2-1.2 2c-4.5.2-9.5-4.8-9.3-9.3z"/></svg>
          (650) 555-0182
        </li>
        <li>
          <svg viewBox="0 0 24 24" aria-hidden="true"><rect class="icon" x="3" y="8" width="18" height="12" rx="1"/><rect class="icon" x="7" y="3" width="10" height="6"/><path class="icon" d="M7 13h10M7 16h6"/></svg>
          (650) 555-0183
        </li>
      </ul>

      <ul class="contact-list details">
        <li>
          <svg viewBox="0 0 24 24" aria-hidden="true"><circle class="icon" cx="12" cy="12" r="10"/><rect class="icon" x="6.5" y="8" width="11" height="8"/><path class="icon" d="M6.5 8l5.5 4.5L17.5 8"/></svg>
          braxo@braxoconstruction.example
        </li>
        <li>
          <svg viewBox="0 0 24 24" aria-hidden="true"><path class="icon" d="M12 22s-7-7.5-7-12.5a7 7 0 0 1 14 0C19 14.5 12 22 12 22z"/><circle class="icon-fill" cx="12" cy="9.5" r="2.5"/></svg>
          <span>LIc 314827, 4158 Garnet Row<br>Cedar Hollow, California 94000</span>
        </li>
        <li>
          <svg viewBox="0 0 24 24" aria-hidden="true"><circle class="icon" cx="12" cy="12" r="10"/><ellipse class="icon" cx="12" cy="12" rx="4.5" ry="10"/><path class="icon" d="M2 12h20M4 7h16M4 17h16"/></svg>
          www.braxoconstruction.example
        </li>
      </ul>
    </div>
  </div>
</body>
</html>
```